Business Recognition Design

We need a design for a recognition to be given to business leaders in our community.
The recognition shall be made on a brass plaque on wood panel background (picture attached, please use it as a background), and all drawing must be in vectors and only one color (black).
It should also have a logo on the top and signature on the right bottom.
The text is enclosed in DOC file.

Reason: just to be able to find the best solution

Reason: None of the suggestion is good enough. Logo in general is too big in comparison with the rest of the plate.

Industry/Entity Type

Business

Requirements
Must have
• - standard Windows font (or possibility to install the same font on Windows), as the name on the recognition shall be printed in the same font
Nice to have
• - some graphic element (in curves) representing achievements in business
- should look great :)

```html
<!DOCTYPE html>
<html lang="en">
<head>
<meta charset="utf-8">
<title>Business Recognition Plaque</title>
<link href="https://fonts.googleapis.com/css2?family=Open+Sans:wght@400;700;800&display=swap" rel="stylesheet">
<style>
  :root {
    --wood-dark: #4e2f16;
    --wood-mid: #7a5030;
    --wood-light: #9a6b44;
    --brass-dark: #b8901c;
    --brass-mid: #d8b53a;
    --brass-light: #f4e486;
    --ink: #111008;
    --ornament: #5a4a14;
    --screw-dark: #8a6a10;
    --screw-light: #f6e69a;
  }
  * { box-sizing: border-box; margin: 0; padding: 0; }
  html, body { width: 1200px; height: 924px; overflow: hidden; background: var(--wood-dark); }
  .plaque {
    position: relative; width: 1200px; height: 924px;
    background: linear-gradient(180deg, var(--wood-mid), var(--wood-light) 50%, var(--wood-mid));
    box-shadow: inset 0 0 0 10px var(--wood-dark), inset 0 0 30px rgba(0,0,0,.5);
    font-family: "Open Sans", Verdana, sans-serif;
    color: var(--ink);
  }
  .plate {
    position: absolute; left: 50px; top: 50px; width: 1100px; height: 826px;
    background:
      repeating-linear-gradient(180deg, rgba(255,255,255,.06) 0 2px, rgba(0,0,0,.04) 2px 4px),
      linear-gradient(160deg, var(--brass-mid) 0%, var(--brass-light) 45%, var(--brass-mid) 70%, var(--brass-dark) 100%);
    box-shadow: 0 0 0 3px #e9d47a, 0 4px 10px rgba(0,0,0,.45);
  }
  .ornament-band { position: absolute; background: var(--ornament); opacity: .85; }
  .ornament-band.top { left: 62px; top: 18px; width: 984px; height: 16px; }
  .ornament-band.bottom { left: 62px; top: 778px; width: 984px; height: 18px; }
  .ornament-band.left { left: 22px; top: 54px; width: 20px; height: 712px; }
  .ornament-band.right { left: 1056px; top: 58px; width: 22px; height: 712px; }
  .screw {
    position: absolute; width: 28px; height: 28px; border-radius: 50%;
    background: radial-gradient(circle at 35% 35%, var(--screw-light), var(--brass-mid) 55%, var(--screw-dark));
    box-shadow: 0 1px 3px rgba(0,0,0,.5);
  }
  .screw.tl { left: 28px; top: 20px; } .screw.tr { left: 1058px; top: 20px; }
  .screw.bl { left: 28px; top: 770px; } .screw.br { left: 1058px; top: 770px; }
  .line { position: absolute; left: 0; width: 100%; text-align: center; white-space: nowrap; }
  .logo-name { top: 80px; font-size: 80px; font-weight: 800; line-height: 1.3; }
  .title-box {
    position: absolute; left: 314px; top: 254px; width: 472px; height: 94px;
    border: 4px solid var(--ink); border-radius: 40px;
    display: flex; align-items: center; justify-content: center;
    font-size: 56px; letter-spacing: 1px;
  }
  .award { top: 392px; font-size: 35px; line-height: 1.4; }
  .award-to { top: 450px; font-size: 35px; line-height: 1.4; }
  .recipient { top: 510px; font-size: 35px; line-height: 1.4; }
  .citation { top: 576px; font-size: 27px; line-height: 41.6px; letter-spacing: .3px; }
  .signature-row { position: absolute; top: 732px; font-size: 26px; line-height: 1.4; }
  .date { left: 260px; }
  .signatory { left: 632px; }
  strong { font-weight: 700; }
</style>
</head>
<body>
<main class="plaque">
  <section class="plate">
    <div class="ornament-band top" role="img" aria-label="Decorative ornamental border"></div>
    <div class="ornament-band bottom" role="img" aria-label="Decorative ornamental border"></div>
    <div class="ornament-band left" role="img" aria-label="Decorative ornamental border"></div>
    <div class="ornament-band right" role="img" aria-label="Decorative ornamental border"></div>
    <span class="screw tl"></span><span class="screw tr"></span>
    <span class="screw bl"></span><span class="screw br"></span>

    <div class="line logo-name">(Our Logo)</div>
    <div class="title-box">RECOGNITION</div>
    <div class="line award">The Best Entrepreneur in 2013</div>
    <div class="line award-to">to</div>
    <div class="line recipient">Mr. <strong>Daniel R. Whitfield,</strong> MBA</div>
    <div class="line citation">
      Under the leadership of Mr. Daniel R. Whitfield, MBA<br>
      the company <strong>DR-WHITFIELD Ltd</strong> has been selected<br>
      by a City Council as the best company of The City.
    </div>
    <div class="signature-row date">Date: 4th July, 2013</div>
    <div class="signature-row signatory">City Mayor</div>
  </section>
</main>
</body>
</html>
```